Design Only - Custom Travel Brand E-Commerce *

I have a basic website layout already made on Shopify, but looking for some additional design touches on a few pages. We would like to add some more style and creativity to the site. The images on the site are not final, just placeholders.

We are a travel brand selling our first 2 items (custom luggage tag & passport wallet). The premise is to engrave the product with everywhere you have been and everywhere you will go. You are allowed to ship back to us and re-engrave new places for $5.

The customizer page is already coded but we can make changes to the forms (select countries, enter contact information form, and overall flow)

Target Market(s)

Millennials and travelers. Most likely more females then males will be purchasing. Also for parents buying children gift cards/gifts

Industry/Entity Type

E-Commerce

Number of Pages Required

5+ page

Font styles to use
Sans Serif

Colors
85cae6
3176b5
acd136

Requirements
Must have
• Looking for ways to add some new design to the pages. It's a new product category so want the customer to fully understand what it is and how it works. The gifting page will be important because you can either buy a blank tag/passport holder as a gift ($5 paid one-time return included) or a gift card from the gifting page.
Nice to have
• Looking to add a bit of color. Gray is ok. Brand is primarily black and white but would be nice to add a TINY pop of color on certain buttons maybe.
Should not have
• The customizer feature is fixed. You can change the form look/feel.

```html
<!DOCTYPE html>
<html lang="en">
<head>
<meta charset="utf-8">
<title>Roamstead — Roampassport</title>
<link href="https://fonts.googleapis.com/css2?family=Poppins:wght@400;500;700&display=swap" rel="stylesheet">
<style>
:root{
  --ink:#1d1d1f;
  --muted:#9aa3ad;
  --soft:#f2f4f6;
  --line:#dfe3e8;
  --price:#3fbf6a;
  --blue:#1e7bf2;
  --red:#f24a4a;
  --turq:#3fddc9;
  --btn:#e9ecef;
  --btn-text:#5b6570;
}
*{box-sizing:border-box;margin:0;padding:0}
html,body{width:1200px;height:1144px;overflow:hidden;background:#fff}
body{font-family:'Poppins',sans-serif;color:var(--ink);position:relative}
.abs{position:absolute}
.nav-link{position:absolute;top:39px;font-size:12.5px;letter-spacing:.4px;color:var(--ink)}
.brand{position:absolute;left:527px;top:29px;width:146px;height:38px;border:2px solid var(--ink);border-radius:3px;display:flex;align-items:center;justify-content:center;font-size:17px;font-weight:500;letter-spacing:3px}
.thumb{position:absolute;left:72px;width:81px;height:81px;background:#e1e3e6;display:flex;align-items:center;justify-content:center}
.thumb.active{background:#c3c5c8}
.product-photo{position:absolute;left:274px;top:155px;width:256px;height:598px;border-radius:10px;background:linear-gradient(180deg,#a9cdd0 0%,#8fbcc0 50%,#4f9597 100%)}
.caption{position:absolute;left:352px;width:100px;top:764px;text-align:center;font-size:15px;color:#3a3a3a}
.title{left:691px;top:138px;font-size:20px;letter-spacing:.6px;font-weight:500}
.price{left:691px;top:177px;font-size:14px;color:var(--price);font-weight:500}
.ship{left:691px;top:218px;font-size:11px;color:var(--muted)}
.label{font-size:13.5px;color:var(--muted)}
.field{position:absolute;border:1px solid var(--line);border-radius:4px;background:#fff}
.select{left:691px;top:309px;width:177px;height:39px;display:flex;align-items:center;padding:0 10px;font-size:14px;color:#3b4450;gap:10px}
.dot{width:20px;height:20px;border-radius:50%;background:var(--turq)}
.search{left:691px;top:424px;width:421px;height:39px;border:1.5px solid #c8cfd6;display:flex;align-items:center;justify-content:space-between;padding:0 2px 0 19px}
.search-btn{width:30px;height:30px;border-radius:4px;background:#eef0f2;display:flex;align-items:center;justify-content:center}
.city{position:absolute;left:691px;width:421px;height:39px;background:var(--soft);border-radius:4px;display:flex;align-items:center;justify-content:space-between;padding:0 4px 0 20px;font-size:14px;color:#5a6470}
.act{width:30px;height:30px;border-radius:4px;display:flex;align-items:center;justify-content:center}
.act.add{background:var(--blue)}
.act.remove{background:var(--red)}
.qty{left:691px;top:683px;width:150px;height:40px;display:flex;align-items:center;justify-content:space-between;padding:0 12px;font-size:13px}
.next{position:absolute;left:691px;top:773px;width:421px;height:38px;background:var(--btn);border-radius:4px;display:flex;align-items:center;justify-content:center;font-size:14px;font-weight:500;color:var(--btn-text);letter-spacing:.2px}
.acc{position:absolute;left:691px;width:421px;display:flex;justify-content:space-between;align-items:center;font-size:14px}
.rule{position:absolute;left:691px;width:421px;height:1px;background:var(--line)}
.desc-h{left:714px;top:907px;font-size:10.5px;color:#5a6470}
.desc{left:714px;top:928px;width:380px;font-size:10px;line-height:15px;color:#5a6470}
.desc em{color:var(--blue);font-weight:700}
</style>
</head>
<body>
<nav>
  <span class="nav-link" style="left:50px">SHOP</span>
  <span class="nav-link" style="left:117px">GIFTING</span>
  <span class="nav-link" style="left:200px">ABOUT US</span>
  <span class="nav-link" style="left:298px">REGISTER YOUR TAG</span>
  <div class="brand">ROAMSTEAD</div>
  <span class="nav-link" style="left:910px;letter-spacing:.8px">ACCOUNT</span>
  <svg class="abs" style="left:991px;top:44px" width="13" height="8" viewBox="0 0 13 8"><path d="M1 1l5.5 5.5L12 1" fill="none" stroke="#1d1d1f" stroke-width="1.6"/></svg>
  <span class="nav-link" style="left:1035px;letter-spacing:.8px">CART (0)</span>
  <svg class="abs" style="left:1131px;top:40px" width="17" height="17" viewBox="0 0 17 17"><circle cx="7" cy="7" r="5.8" fill="none" stroke="#1d1d1f" stroke-width="1.6"/><path d="M11.3 11.3L16 16" stroke="#1d1d1f" stroke-width="1.6"/></svg>
</nav>

<div class="gallery">
  <div class="thumb active" style="top:143px"><svg width="38" height="40" viewBox="0 0 38 40"><path d="M13 12l6-6 6 6" fill="none" stroke="#fff" stroke-width="2"/><rect x="2" y="14" width="34" height="24" fill="none" stroke="#fff" stroke-width="3"/><path d="M7 34l8-9 6 6 5-4 6 7z" fill="#fff"/></svg></div>
  <div class="thumb" style="top:236px"><svg width="38" height="40" viewBox="0 0 38 40"><path d="M13 12l6-6 6 6" fill="none" stroke="#fff" stroke-width="2"/><rect x="2" y="14" width="34" height="24" fill="none" stroke="#fff" stroke-width="3"/><path d="M7 34l8-9 6 6 5-4 6 7z" fill="#fff"/></svg></div>
  <div class="thumb" style="top:328px"><svg width="38" height="40" viewBox="0 0 38 40"><path d="M13 12l6-6 6 6" fill="none" stroke="#fff" stroke-width="2"/><rect x="2" y="14" width="34" height="24" fill="none" stroke="#fff" stroke-width="3"/><path d="M7 34l8-9 6 6 5-4 6 7z" fill="#fff"/></svg></div>
  <div class="thumb" style="top:420px"><svg width="38" height="40" viewBox="0 0 38 40"><path d="M13 12l6-6 6 6" fill="none" stroke="#fff" stroke-width="2"/><rect x="2" y="14" width="34" height="24" fill="none" stroke="#fff" stroke-width="3"/><path d="M7 34l8-9 6 6 5-4 6 7z" fill="#fff"/></svg></div>
  <div class="product-photo" role="img" aria-label="Turquoise leather luggage tag with strap, engraved with travel destinations"></div>
  <div class="caption">Front</div>
</div>

<section class="details">
  <h1 class="abs title">ROAMPASSPORT</h1>
  <p class="abs price">$ 65.00</p>
  <p class="abs ship">* Free shipping Worldwide</p>

  <span class="abs label" style="left:711px;top:284px">Color</span>
  <div class="field select"><span class="dot"></span><span style="flex:1">Turquoise</span>
    <svg width="13" height="8" viewBox="0 0 13 8"><path d="M1 1l5.5 5.5L12 1" fill="none" stroke="#3b4450" stroke-width="1.6"/></svg></div>
  <span class="abs label" style="left:909px;top:284px">Add Initials (+$10)</span>
  <div class="field" style="left:889px;top:309px;width:223px;height:39px"></div>

  <div class="field search"><span style="font-size:15px;color:#3b4450">|</span>
    <span class="search-btn"><svg width="13" height="13" viewBox="0 0 13 13"><circle cx="5.5" cy="5.5" r="4.3" fill="none" stroke="#5b6570" stroke-width="1.3"/><path d="M8.7 8.7L12 12" stroke="#5b6570" stroke-width="1.3"/></svg></span></div>

  <div class="city" style="top:474px">Tokyo<span class="act add"><svg width="14" height="14"><path d="M7 1v12M1 7h12" stroke="#fff" stroke-width="1.6"/></svg></span></div>
  <div class="city" style="top:521px">Los Angeles<span class="act add"><svg width="14" height="14"><path d="M7 1v12M1 7h12" stroke="#fff" stroke-width="1.6"/></svg></span></div>
  <div class="city" style="top:569px">Manila<span class="act remove"><svg width="12" height="12"><path d="M1 1l10 10M11 1L1 11" stroke="#fff" stroke-width="1.6"/></svg></span></div>

  <span class="abs label" style="left:711px;top:659px">Quantity</span>
  <div class="field qty">
    <svg width="16" height="2"><path d="M0 1h16" stroke="#3b4450" stroke-width="1.6"/></svg>
    <span>1</span>
    <svg width="16" height="16"><path d="M8 0v16M0 8h16" stroke="#3b4450" stroke-width="1.6"/></svg>
  </div>

  <div class="next">Next Step: Enter ID Your Information</div>

  <div class="acc" style="top:861px">Product details
    <svg width="11" height="7" viewBox="0 0 11 7"><path d="M1 6l4.5-4.5L10 6" fill="none" stroke="#1d1d1f" stroke-width="1.8"/></svg></div>
  <div class="rule" style="top:891px;background:#3b4450"></div>
  <p class="abs desc-h">Description</p>
  <p class="abs desc">The most customizable luggage tag in the world. <em>Show the world where you've been.</em> This customizable luggage tag allows you to engrave your favorite destinations.</p>
  <div class="rule" style="top:994px;left:714px;width:398px"></div>

  <div class="acc" style="top:1014px">FAQ
    <svg width="11" height="7" viewBox="0 0 11 7"><path d="M1 1l4.5 4.5L10 1" fill="none" stroke="#1d1d1f" stroke-width="1.8"/></svg></div>
  <div class="rule" style="top:1044px"></div>
  <div class="acc" style="top:1064px">Review
    <svg width="11" height="7" viewBox="0 0 11 7"><path d="M1 1l4.5 4.5L10 1" fill="none" stroke="#1d1d1f" stroke-width="1.8"/></svg></div>
  <div class="rule" style="top:1094px"></div>
</section>
</body>
</html>
```